Wordpress Layout, Plug-in, Mash-up Overhaul

We have collection of vertical topic portals; in each portal, a post typically is an article which goes with a subject video, following are 5 reference sites:

http://www.ledgerbrook.com/
http://www.velmacounsel.com/
http://www.shimmerlane.tv/
http://www.nestharbor.com/
http://www.ladiestalkly.com/

We obtained most of our based WP theme from various premium WP template membership sites, subsequently re-organise, mash-up content to produce sites as above; however we start to be constraint as we get into a fixed pattern of laying out our contents and we seeking professional help to re-work this. these re-work can includes as follows.

1. proposal on creative re-placement of component / re-layout on the templates. Should also suggest different way for the advertising banner placement etc.

2. proposal on right and appropriate use of WP plugins (paid or free but have to be secured and reliable) to achieve more relevant add-on of content where necessary (rss, etc)

Objective:
We want to move away from our internal team design constraint and also moving alway from being stuck with certain stereo-type way of WP content site. However the proposed WP design should still be a portal-centric type vs blogging/product-centric.

Deliverables:
1. We don't need the actual cut template but a design mockup of the home page and relevant sub pages (.psd, jpg etc) for the proposed re-design. Based on the above 5 listed sites, the deliverable would be at least 10 pages of design layout work (considering home page and 1 sub pages for each domain; could be more if necessary)

2. The plugins reference where necessary

What's expected from your proposal for the bid:
We would like a mockup of a re-design from any pick from any of the above 5 domains

```html
<!DOCTYPE html>
<html lang="en">
<head>
<meta charset="utf-8">
<title>Ladies Talkly — Home</title>
<link rel="stylesheet" href="https://fonts.googleapis.com/css2?family=Lato:ital,wght@0,400;0,700;0,900;1,700;1,900&family=PT+Sans+Narrow:wght@700&family=PT+Sans:wght@700&family=Yesteryear&display=swap">
<style>
:root{
  --purple:#9b3ea9;
  --purple-head:#8a3898;
  --yellow:#f6c21a;
  --ticker-bg:#fdf2c4;
  --ink:#222222;
  --text:#444444;
  --rule:#cfcfcf;
  --ad-bg:#f2f2f2;
  --white:#ffffff;
  --bar:#444444;
  --net-friends:#3b5a9a;
  --net-video:#d12b27;
  --net-feed:#f39a1e;
  --net-pins:#c8202d;
  --tag-fashion:#2f8a2a;
  --tag-beauty:#1eaab0;
  --tag-diet:#e0239c;
  --tag-food:#e97d22;
  --tag-travel:#1f5b8d;
  --tag-health:#44a547;
  --tag-love:#d7262c;
}
*{box-sizing:border-box;margin:0;padding:0}
html,body{width:1200px;height:2564px;overflow:hidden}
body{position:relative;font-family:'Lato',sans-serif;color:var(--text);background:#8a4f9c}
.backdrop{position:absolute;inset:0;background:linear-gradient(90deg,#6d3f86 0%,#b590c9 4%,#8e5aa3 6.5%,#8e5aa3 93.5%,#f1d6ef 96%,#c99fd6 100%)}
.backdrop::after{content:"";position:absolute;inset:0;background:radial-gradient(circle at 97% 6%,#fff7c9 0,transparent 9%),radial-gradient(circle at 2% 40%,#c8b4e0 0,transparent 10%),radial-gradient(circle at 98% 60%,#f4d0f0 0,transparent 12%)}
.site{position:absolute;left:73px;top:0;width:1055px;height:2150px;background:var(--white)}
/* header */
.brand{position:absolute;left:99px;top:16px;display:flex;align-items:center;gap:9px}
.brand-dot{width:30px;height:30px;border-radius:50%;background:var(--yellow)}
.brand-name{font-family:'PT Sans',sans-serif;font-weight:700;font-size:25px;line-height:25px;color:var(--purple);width:100px}
.ad{position:absolute;background:var(--ad-bg);display:flex;align-items:center;justify-content:center;font-size:11px;color:#b8b8b8}
.mainnav{position:absolute;left:73px;top:97px;width:1055px;height:47px;background:var(--purple);display:flex;align-items:center;padding-left:43px}
.mainnav a{font-family:'PT Sans Narrow',sans-serif;font-weight:700;font-size:15px;color:var(--white);text-decoration:none;margin-right:36px;text-transform:uppercase;position:relative;line-height:47px}
.mainnav a.current{color:var(--yellow)}
.mainnav a.current::after{content:"";position:absolute;left:0;right:0;bottom:8px;height:2px;background:var(--yellow)}
.search-icon{position:absolute;right:22px;top:14px}
/* media placeholders */
.photo{position:absolute;overflow:hidden}
.caption{position:absolute;left:16px;bottom:14px;right:12px}
.tag{display:inline-block;font-family:'Lato',sans-serif;font-weight:700;font-size:8.5px;line-height:1;color:var(--white);padding:3px 5px;text-transform:uppercase;letter-spacing:.2px}
.tag.fashion{background:var(--tag-fashion)}
.tag.beauty{background:var(--tag-beauty)}
.tag.diet{background:var(--tag-diet)}
.tag.food{background:var(--tag-food)}
.tag.travel{background:var(--tag-travel)}
.tag.health{background:var(--tag-health)}
.tag.love{background:var(--tag-love)}
.caption h3{font-family:'Lato',sans-serif;font-style:italic;font-weight:900;color:var(--white);margin-top:7px;line-height:1.15}
/* ticker */
.ticker{position:absolute;left:99px;top:492px;width:1000px;height:31px;background:var(--ticker-bg);display:flex;align-items:center;overflow:hidden;white-space:nowrap}
.ticker-label{height:31px;background:var(--yellow);color:var(--white);font-family:'Yesteryear',cursive;font-size:17px;display:flex;align-items:center;padding:0 14px 0 16px;position:relative;margin-right:22px}
.ticker-label::after{content:"";position:absolute;right:-10px;top:0;border-left:10px solid var(--yellow);border-top:15.5px solid transparent;border-bottom:15.5px solid transparent}
.ticker span.item{font-family:'Lato',sans-serif;font-style:italic;font-weight:700;font-size:12px;color:var(--ink);margin-right:10px}
.ticker i{display:inline-block;width:5px;height:5px;background:var(--yellow);margin-right:10px;vertical-align:middle}
/* section headings */
.section-head{position:absolute;left:99px;width:660px;font-family:'PT Sans Narrow',sans-serif;font-weight:700;font-size:18px;color:var(--purple-head);text-transform:uppercase;border-bottom:2px solid #a9a9a9;padding-bottom:4px;line-height:1}
.post-title{font-family:'Lato',sans-serif;font-weight:900;font-style:italic;color:var(--ink);line-height:1.2}
.excerpt{font-size:13px;line-height:20px;color:var(--text)}
.more{color:var(--yellow);font-weight:700;font-style:italic;font-size:10.5px}
.feature{position:absolute;left:99px;width:660px;height:149px}
.feature .photo{left:0;top:0;width:226px;height:149px}
.feature .body{position:absolute;left:243px;top:0;right:0}
.feature .excerpt{line-height:19.5px}
.dash{position:absolute;left:99px;width:660px;border-top:1px dashed var(--rule)}
.trend{position:absolute;width:318px}
.trend .photo{position:relative;width:318px;height:169px;display:block}
.trend .tag{margin-top:11px}
.trend .post-title{font-size:15.5px;margin:8px 0 3px}
.trend .excerpt{line-height:19px}
.mini{position:absolute;width:318px;height:73px}
.mini .photo{left:0;top:0;width:73px;height:73px}
.mini .body{position:absolute;left:85px;top:6px}
.mini .post-title{font-size:13px;margin-top:5px}
.tile{position:absolute;width:202px}
.tile .photo{position:relative;display:block;width:202px;height:108px}
.tile .tag{margin-top:11px}
.tile .post-title{font-size:13px;margin-top:5px}
.arrow{position:absolute;width:12px;height:28px;background:rgba(255,255,255,.55);display:flex;align-items:center;justify-content:center}
/* sidebar */
.widget-head{position:absolute;left:801px;width:299px;display:flex;align-items:center;gap:6px;font-family:'Yesteryear',cursive;font-weight:400;font-size:19px;color:var(--purple);line-height:1}
.widget-head .stripes{flex:1;height:10px;background:repeating-linear-gradient(135deg,#d6b0dc 0 2px,transparent 2px 5px)}
.about{position:absolute;left:801px;top:590px;width:299px;font-size:11.3px;line-height:18px;color:var(--text)}
.social{position:absolute;display:flex;align-items:center;gap:10px}
.net{width:46px;height:46px;display:flex;align-items:center;justify-content:center;font-family:'Lato',sans-serif;font-weight:700;font-size:9px;color:var(--white);text-transform:uppercase;letter-spacing:.3px}
.net.friends{background:var(--net-friends)}
.net.video{background:var(--net-video)}
.net.feed{background:var(--net-feed)}
.net.pins{background:var(--net-pins)}
.social b{display:block;font-family:'Lato',sans-serif;font-weight:900;font-size:23px;color:var(--ink);line-height:1}
.social small{display:block;font-size:8px;color:var(--text);letter-spacing:.4px;margin-top:3px}
.pop{position:absolute;left:801px;width:299px;height:132px}
.pop .caption h3{font-size:13px}
.pop .caption{left:16px;bottom:10px}
.pop .tag{position:absolute;left:0;top:5px}
.news{position:absolute;left:801px;top:1656px;width:299px;list-style:none}
.news li{font-size:11.3px;line-height:16px;color:var(--text);padding-left:9px;position:relative;margin-bottom:6px}
.news li::before{content:"";position:absolute;left:0;top:7px;width:3px;height:3px;border-radius:50%;background:var(--ink)}
/* footer */
.footer{position:absolute;left:73px;top:2150px;width:1055px;height:385px;background:var(--purple)}
.foot-head{position:absolute;font-family:'Yesteryear',cursive;font-weight:400;font-size:19px;color:var(--yellow);width:316px;border-bottom:1px solid rgba(255,255,255,.3);padding-bottom:4px;line-height:1}
.foot-head span{display:inline-block;border-bottom:2px solid var(--yellow);padding-bottom:3px;margin-bottom:-7px}
.foot-item{position:absolute;width:316px;height:76px;border-bottom:1px dashed rgba(255,255,255,.35)}
.foot-item .photo{left:0;top:0;width:73px;height:73px}
.foot-item .body{position:absolute;left:85px;top:4px;right:0}
.foot-item .post-title{font-size:13px;color:var(--white);margin-top:5px}
.foot-social{position:absolute;left:784px;top:2446px;display:flex;gap:10px}
.foot-social .net{width:44px;height:44px}
.bottombar{position:absolute;left:73px;top:2535px;width:1055px;height:29px;background:var(--bar);display:flex;align-items:center;justify-content:space-between;padding:0 30px 0 26px}
.bottombar p{font-size:10.5px;color:#cfcfcf}
.bottombar nav a{font-size:9.5px;color:#e6e6e6;text-transform:uppercase;text-decoration:none;margin-left:18px;font-weight:700}
.to-top{position:absolute;left:1154px;top:2538px;width:26px;height:26px;background:#5a5a5a;display:flex;align-items:center;justify-content:center}
</style>
</head>
<body>
<div class="backdrop" role="img" aria-label="Lavender field with soft pink and violet light bokeh"></div>
<div class="site"></div>

<header>
  <div class="brand"><div class="brand-dot"></div><div class="brand-name">Ladies Talkly</div></div>
  <div class="ad" style="left:461px;top:9px;width:639px;height:78px">Leaderboard Ad (728 x 90)</div>
  <nav class="mainnav">
    <a class="current" href="#">Home</a><a href="#">Beauty</a><a href="#">Fashion</a><a href="#">Love &amp; Relationships</a><a href="#">Travel</a><a href="#">Food</a><a href="#">Diet &amp; Fitness</a><a href="#">Health</a>
    <svg class="search-icon" width="16" height="16" viewBox="0 0 16 16"><circle cx="6.5" cy="6.5" r="4.8" fill="none" stroke="#fff" stroke-width="2"/><line x1="10" y1="10" x2="14.5" y2="14.5" stroke="#fff" stroke-width="2.4" stroke-linecap="round"/></svg>
  </nav>
</header>

<section class="slider">
  <div class="photo" style="left:73px;top:147px;width:21px;height:337px;background:linear-gradient(#8d8d8d,#5d5d5d)" role="img" aria-label="Edge of the previous slide"></div>
  <div class="photo" style="left:99px;top:147px;width:499px;height:337px;background:linear-gradient(180deg,#5a9ad8 0%,#8cc0ea 45%,#c9a27a 70%,#5b4a3e 100%)" role="img" aria-label="Four friends in bikinis raising drinks by a seaside railing">
    <div class="caption"><span class="tag fashion">Fashion</span><h3 style="font-size:20px">How to Choose Flattering Bikinis</h3></div>
  </div>
  <div class="photo" style="left:602px;top:147px;width:246px;height:337px;background:linear-gradient(160deg,#d9cfc8 0%,#b88c72 50%,#4a3328 100%)" role="img" aria-label="Woman with long loose wavy hair">
    <div class="caption"><span class="tag beauty">Beauty</span><h3 style="font-size:14px">How to Style Loose Waves</h3></div>
  </div>
  <div class="photo" style="left:853px;top:147px;width:246px;height:165px;background:linear-gradient(160deg,#d7efe0 0%,#d23a2e 45%,#7a2b22 100%)" role="img" aria-label="Fresh vegetables and a measuring tape on a plate">
    <div class="caption" style="bottom:10px"><span class="tag diet">Diet &amp; Fitness</span><h3 style="font-size:13.5px">How to Lose Weight in 2 Weeks with Nutrition</h3></div>
  </div>
  <div class="photo" style="left:853px;top:318px;width:246px;height:166px;background:linear-gradient(160deg,#f3d58d 0%,#d9a23e 50%,#7d5420 100%)" role="img" aria-label="Golden crispy fried chicken pieces">
    <div class="caption" style="bottom:10px"><span class="tag food">Food</span><h3 style="font-size:14px">Crispy Chicken Recipe</h3></div>
  </div>
  <div class="photo" style="left:1111px;top:147px;width:17px;height:337px;background:linear-gradient(#9a9a9a,#5a5a5a)" role="img" aria-label="Edge of the next slide"></div>
</section>

<div class="ticker">
  <div class="ticker-label">The Latest</div>
  <span class="item">How to Protect Skin from Sun</span><i></i>
  <span class="item">How to Rejuvenate Skin</span><i></i>
  <span class="item">How to Wear A Little Black Dress</span><i></i>
  <span class="item">How to Know When to Consider A Divorce</span><i></i>
  <span class="item">How to</span>
</div>

<main>
  <h2 class="section-head" style="top:557px">Featured Topics</h2>
  <article class="feature" style="top:600px">
    <div class="photo" style="background:linear-gradient(160deg,#c5dfe8 0%,#a9c98b 55%,#6f9a4c 100%)" role="img" aria-label="Women stretching outdoors during a pilates class"></div>
    <div class="body">
      <span class="tag diet">Diet &amp; Fitness</span>
      <h3 class="post-title" style="font-size:15.5px;margin:7px 0 3px">How to Do 10 Minute Pilates</h3>
      <p class="excerpt">Pilates is a very popular form of exercise due to its many benefits. With Pilates, the whole core is strengthened. Also, great posture, flexibility, and balance are developed at the same time. With all of these benefits, it's no wonder why its so popular. With many people having busy schedules, they may think that they don't… <span class="more">Learn More »</span></p>
    </div>
  </article>
  <div class="dash" style="top:767px"></div>
  <article class="feature" style="top:785px">
    <div class="photo" style="background:radial-gradient(circle at 50% 50%,#f2e9ea 0,#5a9bd6 45%,#1c4b85 100%)" role="img" aria-label="Woman in winter makeup among falling snow"></div>
    <div class="body">
      <span class="tag beauty">Beauty</span>
      <h3 class="post-title" style="font-size:15.5px;margin:7px 0 3px">How to Do Cool Winter Makeup</h3>
      <p class="excerpt">Winter is a festive time, and in many parts of the world, it means snow is falling and Santa Claus is coming to town. Styles and fashions change as well. As some areas of the world get colder, boots, winter coats, scarves, hats, mittens and muffs are a must. But what about makeup? Well, that changes too. Here's how to master a… <span class="more">Learn More »</span></p>
    </div>
  </article>
  <div class="dash" style="top:951px"></div>

  <h2 class="section-head" style="top:1003px">Fall 2014 Trends</h2>
  <article class="trend" style="left:99px;top:1046px">
    <div class="photo" style="background:linear-gradient(150deg,#3a1c2a 0%,#b23a4e 45%,#e9a9a0 70%,#2a1320 100%)" role="img" aria-label="Group of women smiling at a night out"></div>
    <span class="tag fashion">Fashion</span>
    <h3 class="post-title">What to Wear on A Girls Night-out</h3>
    <p class="excerpt">Everyone loves that moment when your phone rings and your girlfriends let you know that it's on. Girls night out is everyone's favorite and once that call comes in the strategic planning of outfits begins. Choosing something that is both fun… <span class="more">Learn More »</span></p>
  </article>
  <article class="trend" style="left:441px;top:1046px">
    <div class="photo" style="background:linear-gradient(150deg,#f0d89a 0%,#c99445 50%,#5e3b17 100%)" role="img" aria-label="Vintage postcards of European landmarks"></div>
    <span class="tag travel">Travel</span>
    <h3 class="post-title">European Destinations on A Budget</h3>
    <p class="excerpt">A European vacation was once limited to the truly wealthy debutantes and heirs. Cheaper travel options have made travelling to Europe within the reach of many. Despite this, there are many different ways to see Europe on a budget at a… <span class="more">Learn More »</span></p>
  </article>
  <article class="mini" style="left:99px;top:1395px">
    <div class="photo" style="background:linear-gradient(150deg,#e8e3e0,#4b5a78)" role="img" aria-label="Woman in loose boyfriend jeans"></div>
    <div class="body"><span class="tag fashion">Fashion</span><h3 class="post-title">3 Ways to Wear Your Boyfriends<br>Clothes</h3></div>
  </article>
  <article class="mini" style="left:441px;top:1395px">
    <div class="photo" style="background:linear-gradient(150deg,#c7d69a,#6e7f3a 60%,#4a3d28)" role="img" aria-label="Tree-lined path through a city park"></div>
    <div class="body"><span class="tag travel">Travel</span><h3 class="post-title">A Guide to Central Park</h3></div>
  </article>
  <div class="dash" style="top:1476px;width:318px"></div>
  <div class="dash" style="top:1476px;left:441px;width:318px"></div>
  <article class="mini" style="left:99px;top:1485px">
    <div class="photo" style="background:linear-gradient(150deg,#f3ece6,#b58a72)" role="img" aria-label="Woman relaxing in a casual outfit"></div>
    <div class="body"><span class="tag fashion">Fashion</span><h3 class="post-title">How to Style A Lazy Day Look</h3></div>
  </article>
  <article class="mini" style="left:441px;top:1485px">
    <div class="photo" style="background:linear-gradient(150deg,#cfd6de,#8a6a52 60%,#3b2e2a)" role="img" aria-label="Busy shopping street in London"></div>
    <div class="body"><span class="tag travel">Travel</span><h3 class="post-title">5 Best Shopping Areas in London</h3></div>
  </article>
  <div class="dash" style="top:1566px;width:318px"></div>
  <div class="dash" style="top:1566px;left:441px;width:318px"></div>

  <h2 class="section-head" style="top:1620px">Healthy Living</h2>
  <article class="tile" style="left:99px;top:1663px">
    <div class="photo" style="background:linear-gradient(150deg,#e7d9cc,#7a5440 60%,#3a2a22)" role="img" aria-label="Woman comforting a sad friend"></div>
    <span class="tag health">Health</span><h3 class="post-title">How to Overcome Depression</h3>
  </article>
  <article class="tile" style="left:328px;top:1663px">
    <div class="photo" style="background:linear-gradient(150deg,#f1ece8,#c0222e 55%,#7d1420)" role="img" aria-label="Slice of layered red velvet cake with a fork"></div>
    <span class="tag food">Food</span><h3 class="post-title">How to Make A Layered Red<br>Velvet Cake</h3>
  </article>
  <article class="tile" style="left:557px;top:1663px">
    <div class="photo" style="background:linear-gradient(150deg,#fbfbfb,#f2b632 50%,#b4481c)" role="img" aria-label="Vitamin capsules spilling from a bottle"></div>
    <span class="tag diet">Diet &amp; Fitness</span><h3 class="post-title">2 Vitamins You Need When You<br>Age</h3>
  </article>
  <div class="arrow" style="left:99px;top:1703px"><svg width="6" height="10" viewBox="0 0 6 10"><path d="M5 1 1 5l4 4" fill="none" stroke="#fff" stroke-width="1.5"/></svg></div>
  <div class="arrow" style="left:747px;top:1703px"><svg width="6" height="10" viewBox="0 0 6 10"><path d="M1 1l4 4-4 4" fill="none" stroke="#fff" stroke-width="1.5"/></svg></div>

  <h2 class="section-head" style="top:1885px">Love &amp; Relationships</h2>
  <article class="tile" style="left:99px;top:1928px">
    <div class="photo" style="background:linear-gradient(150deg,#e9e1d8,#9d7358 55%,#4a3226)" role="img" aria-label="Couple with an interfering mother-in-law"></div>
    <span class="tag love">Love &amp; Relationships</span><h3 class="post-title">How to Best Cope with Interfering<br>in Laws</h3>
  </article>
  <article class="tile" style="left:328px;top:1928px">
    <div class="photo" style="background:linear-gradient(150deg,#d9c2ac,#9a6b49 55%,#523624)" role="img" aria-label="Young woman arguing with her parents"></div>
    <span class="tag love">Love &amp; Relationships</span><h3 class="post-title">How to Handle Difficult Parents</h3>
  </article>
  <article class="tile" style="left:557px;top:1928px">
    <div class="photo" style="background:linear-gradient(150deg,#f4f4f4,#b9a79a 55%,#5f4a3e)" role="img" aria-label="Upset couple sitting apart"></div>
    <span class="tag love">Love &amp; Relationships</span><h3 class="post-title">How to Know When to Consider A<br>Divorce</h3>
  </article>
  <div class="arrow" style="left:99px;top:1968px"><svg width="6" height="10" viewBox="0 0 6 10"><path d="M5 1 1 5l4 4" fill="none" stroke="#fff" stroke-width="1.5"/></svg></div>
  <div class="arrow" style="left:747px;top:1968px"><svg width="6" height="10" viewBox="0 0 6 10"><path d="M1 1l4 4-4 4" fill="none" stroke="#fff" stroke-width="1.5"/></svg></div>
</main>

<aside>
  <h2 class="widget-head" style="top:561px">About Us <span class="stripes"></span></h2>
  <p class="about">Fashion is not the only thing that will be discussed on our website. Fashion is a big part of many women's life, but of course, it is not the most important thing in life. That is why we strive to provide other useful information that will help you in your daily life.You will be able to find information about simple adjustments… <span class="more">Learn More »</span></p>

  <h2 class="widget-head" style="top:729px">Connect with Us <span class="stripes"></span></h2>
  <div class="social" style="left:801px;top:759px"><div class="net friends">Like</div><div><b>8,532</b><small>FOLLOWERS</small></div></div>
  <div class="social" style="left:951px;top:759px"><div class="net video">Watch</div><div><b>2,253</b><small>SUBSCRIBE</small></div></div>
  <div class="social" style="left:801px;top:817px"><div class="net feed"><svg width="18" height="18" viewBox="0 0 18 18" aria-hidden="true"><circle cx="3" cy="15" r="2.2" fill="#fff"/><path d="M1.5 8.5a8 8 0 0 1 8 8M1.5 2.5a14 14 0 0 1 14 14" fill="none" stroke="#fff" stroke-width="2.4"/></svg></div><div><b>RSS</b><small>FEEDS</small></div></div>
  <div class="social" style="left:951px;top:817px"><div class="net pins">Pin</div><div><b>3,502</b><small>FOLLOWERS</small></div></div>

  <div class="ad" style="left:820px;top:896px;width:264px;height:219px">Medium Rectangle Ad (300 x 250)</div>

  <h2 class="widget-head" style="top:1152px">Popular Topics <span class="stripes"></span></h2>
  <div class="photo pop" style="top:1181px;background:linear-gradient(160deg,#3a2a20 0%,#b0692c 50%,#1e1612 100%)" role="img" aria-label="Plate of beef chow mein noodles">
    <span class="tag food">Food</span><div class="caption"><h3>How to Cook Beef Chow Mein</h3></div>
  </div>
  <div class="photo pop" style="top:1321px;background:linear-gradient(180deg,#7db8e6 0%,#bcd9ee 45%,#d9b98d 75%,#8a6a4a 100%)" role="img" aria-label="Couple sunbathing on beach chairs">
    <span class="tag beauty">Beauty</span><div class="caption"><h3>How to Protect Skin From Sun</h3></div>
  </div>
  <div class="photo pop" style="top:1461px;background:linear-gradient(160deg,#e9eef3 0%,#9fb2c9 50%,#3a4a60 100%)" role="img" aria-label="Person lying down holding an injured ankle">
    <span class="tag health">Health</span><div class="caption"><h3>How to Treat An Ankle Fracture</h3></div>
  </div>

  <h2 class="widget-head" style="top:1628px">More News <span class="stripes"></span></h2>
  <ul class="news">
    <li>Will You Shell Out $50K for Marcel Duvant's First Bag Designed for Maison Verel?</li>
    <li>Another Crown of Ashes Star Lands a Major Fall Fashion Campaign with Carla Mendt</li>
    <li>Best of the Red Carpet: The Standout Styles from the 2014 Starlight Awards</li>
    <li>Vena Lorre's Fall 2014 Campaign Gives Us an Unexpected Look at the Unconventional Bride</li>
    <li>Juniper &amp; Cole Uses a Simple Silhouette for a Blogger-Worthy Fall Collection</li>
  </ul>

  <div class="ad" style="left:820px;top:1882px;width:264px;height:218px">Medium Rectangle Ad (300 x 250)</div>
</aside>

<footer>
  <div class="footer"></div>
  <h2 class="foot-head" style="left:99px;top:2188px"><span>Recent Posts</span></h2>
  <article class="foot-item" style="left:99px;top:2232px">
    <div class="photo" style="background:linear-gradient(150deg,#e6ddd6,#8c6a55)" role="img" aria-label="Mother and child on a plane"></div>
    <div class="body"><span class="tag travel">Travel</span><h3 class="post-title">How to Reduce Stress During Air Travel with Your Family</h3></div>
  </article>
  <article class="foot-item" style="left:99px;top:2323px">
    <div class="photo" style="background:linear-gradient(150deg,#6a5a54,#2a201e)" role="img" aria-label="Woman dressed for a date night"></div>
    <div class="body"><span class="tag fashion">Fashion</span><h3 class="post-title">How to Get A Date Night Look</h3></div>
  </article>
  <article class="foot-item" style="left:99px;top:2413px;border:none">
    <div class="photo" style="background:linear-gradient(150deg,#f1e4c6,#c48a3c 55%,#7a4a22)" role="img" aria-label="Baked moussaka in a dish"></div>
    <div class="body"><span class="tag food">Food</span><h3 class="post-title">How to Make Homemade Moussaka</h3></div>
  </article>

  <h2 class="foot-head" style="left:441px;top:2188px"><span>Hot Topics</span></h2>
  <article class="foot-item" style="left:441px;top:2232px">
    <div class="photo" style="background:linear-gradient(150deg,#efe4dc,#a47a62)" role="img" aria-label="Woman covering her mouth"></div>
    <div class="body"><span class="tag health">Health</span><h3 class="post-title">How to Get Rid of Bad Breath</h3></div>
  </article>
  <article class="foot-item" style="left:441px;top:2323px">
    <div class="photo" style="background:linear-gradient(150deg,#d6c3ae,#7a5a40)" role="img" aria-label="Woman with sleek red carpet hair"></div>
    <div class="body"><span class="tag beauty">Beauty</span><h3 class="post-title">Sleek Red Carpet Hair Tutorial</h3></div>
  </article>
  <article class="foot-item" style="left:441px;top:2413px;border:none">
    <div class="photo" style="background:linear-gradient(150deg,#f6eee6,#9fc36a 60%,#d84a36)" role="img" aria-label="Woman holding fresh fruit"></div>
    <div class="body"><span class="tag diet">Diet &amp; Fitness</span><h3 class="post-title">How to Improve Your Skin with Food And Drink</h3></div>
  </article>

  <h2 class="foot-head" style="left:784px;top:2188px"><span>You May Be Interested in</span></h2>
  <div class="photo" style="left:784px;top:2232px;width:316px;height:132px;background:linear-gradient(180deg,#6fa8dc 0%,#b9d4ec 45%,#7c8e9a 75%,#3d4a3a 100%)" role="img" aria-label="Fairy-tale castle at a theme park">
    <span class="tag travel" style="position:absolute;left:0;top:5px">Travel</span>
    <div class="caption" style="bottom:10px"><h3 style="font-size:13px">Castle Park Vacations</h3></div>
  </div>

  <h2 class="foot-head" style="left:784px;top:2402px"><span>Stay Connected</span></h2>
  <div class="foot-social">
    <div class="net friends">Like</div>
    <div class="net video">Watch</div>
    <div class="net feed"><svg width="17" height="17" viewBox="0 0 18 18" aria-hidden="true"><circle cx="3" cy="15" r="2.2" fill="#fff"/><path d="M1.5 8.5a8 8 0 0 1 8 8M1.5 2.5a14 14 0 0 1 14 14" fill="none" stroke="#fff" stroke-width="2.4"/></svg></div>
    <div class="net pins">Pin</div>
  </div>

  <div class="bottombar">
    <p>©2014 LadiesTalkly.</p>
    <nav><a href="#">About Us</a><a href="#">Advertise With Us</a><a href="#">Contact Us</a><a href="#">Privacy Policy</a><a href="#">Sitemap</a></nav>
  </div>
  <div class="to-top"><svg width="10" height="7" viewBox="0 0 10 7"><path d="M1 6l4-4 4 4" fill="none" stroke="#ddd" stroke-width="1.5"/></svg></div>
</footer>
</body>
</html>
```